BUsiness Card

We need a unique business card design for a new aesthetic practice, Meadowlark Aesthetics & Wellness, P.A. The reverse of the card should be an appointment card.

```html
<!DOCTYPE html>
<html lang="en">
<head>
<meta charset="utf-8">
<title>Meadowlark Aesthetics &amp; Wellness – Business Card</title>
<link href="https://fonts.googleapis.com/css2?family=Marcellus&family=Poppins:wght@400;500&display=swap" rel="stylesheet">
<style>
  :root {
    --backdrop: #2a2a2b;
    --navy: #0b4666;
    --teal: #19a49a;
    --paper: #ffffff;
    --mist: #dcdde2;
    --ink: #3a3d42;
    --rule: rgba(255,255,255,.55);
  }
  * { box-sizing: border-box; margin: 0; padding: 0; }
  html, body { width: 1200px; height: 900px; overflow: hidden; background: var(--backdrop); }
  .stage {
    width: 1200px; height: 900px;
    display: flex; align-items: center; justify-content: center; gap: 50px;
  }
  .card {
    position: relative;
    width: 540px; height: 310px;
    border-radius: 18px;
    overflow: hidden;
  }

  /* front */
  .card--front { background: var(--paper); }
  .front__band {
    position: absolute; left: 0; right: 0; bottom: 0; height: 26px;
    background: var(--navy);
  }
  .front__slash { position: absolute; left: 0; bottom: 0; width: 540px; height: 26px; }
  .brand { position: absolute; left: 34px; top: 62px; width: 230px; height: 170px; }
  .brand__disc {
    position: absolute; left: 70px; top: 0; width: 160px; height: 160px;
    border-radius: 50%; background: var(--mist); opacity: .75;
  }
  .brand__name {
    position: absolute; left: 0; top: 52px;
    font-family: "Marcellus", serif; font-weight: 400;
    color: var(--navy); line-height: 1.05;
  }
  .brand__name .big { display: block; font-size: 34px; letter-spacing: .5px; }
  .brand__name .small { display: block; font-size: 13.5px; letter-spacing: 1.6px; margin-top: 6px; text-transform: uppercase; }

  .divider { position: absolute; left: 280px; width: 2px; }
  .divider--navy { top: 48px; height: 62px; background: var(--navy); }
  .divider--teal { top: 122px; height: 22px; background: var(--teal); }
  .divider--grey { top: 158px; height: 80px; background: var(--navy); opacity: .6; }

  .details { position: absolute; left: 298px; top: 46px; right: 20px; }
  .person__name {
    font-family: "Marcellus", serif; font-weight: 400; font-size: 27px; line-height: 1;
    text-transform: uppercase; letter-spacing: .5px; white-space: nowrap;
  }
  .person__first { color: var(--navy); }
  .person__last { color: var(--teal); }
  .person__role { font-family: "Poppins", sans-serif; font-size: 12px; color: var(--ink); margin-top: 5px; }
  .address { font-family: "Poppins", sans-serif; font-size: 12px; color: var(--ink); line-height: 1.45; margin-top: 16px; }
  .contacts { list-style: none; margin-top: 14px; }
  .contacts li {
    display: flex; align-items: center; gap: 8px;
    font-family: "Poppins", sans-serif; font-size: 12px; color: var(--ink); line-height: 1.6;
  }
  .contacts svg { width: 11px; height: 11px; fill: var(--navy); flex: none; }

  /* back – appointment card */
  .card--back { background: var(--navy); color: var(--paper); }
  .back__disc {
    position: absolute; right: -40px; top: 40px; width: 230px; height: 230px;
    border-radius: 50%; background: #ffffff; opacity: .1;
  }
  .back__name {
    position: absolute; left: 36px; top: 30px;
    font-family: "Marcellus", serif; font-weight: 400; line-height: 1.05;
  }
  .back__name .big { display: block; font-size: 30px; letter-spacing: .5px; }
  .back__name .small { display: block; font-size: 11.5px; letter-spacing: 2px; margin-top: 5px; text-transform: uppercase; }
  .appointment { position: absolute; left: 36px; right: 36px; top: 118px; }
  .appointment__title {
    font-family: "Marcellus", serif; font-weight: 400; font-size: 16px;
    letter-spacing: 2px; text-transform: uppercase; color: var(--teal);
  }
  .appointment__note { font-family: "Poppins", sans-serif; font-size: 11px; opacity: .8; margin-top: 3px; }
  .fields { list-style: none; margin-top: 14px; display: grid; grid-template-columns: 1fr 1fr; gap: 16px 28px; }
  .fields li {
    display: flex; align-items: flex-end; gap: 8px;
    font-family: "Poppins", sans-serif; font-size: 12px;
  }
  .fields .line { flex: 1; border-bottom: 1px solid var(--rule); height: 14px; }
  .back__band { position: absolute; left: 0; right: 0; bottom: 0; height: 26px; background: var(--teal); opacity: .85; }
</style>
</head>
<body>
<main class="stage">
  <section class="card card--front" aria-label="Business card front">
    <div class="brand">
      <div class="brand__disc"></div>
      <p class="brand__name"><span class="big">Meadowlark</span><span class="small">Aesthetics &amp; Wellness</span></p>
    </div>

    <span class="divider divider--navy"></span>
    <span class="divider divider--teal"></span>
    <span class="divider divider--grey"></span>

    <div class="details">
      <h1 class="person__name"><span class="person__first">Daniel</span> <span class="person__last">Hartley</span></h1>
      <p class="person__role">Founder &amp; CEO</p>
      <p class="address">Linden Row, Ashford<br>Kent, TN24 8QP</p>
      <ul class="contacts">
        <li><svg viewBox="0 0 24 24"><path d="M6.6 10.8a15 15 0 0 0 6.6 6.6l2.2-2.2a1 1 0 0 1 1-.25 11.4 11.4 0 0 0 3.6.57 1 1 0 0 1 1 1V20a1 1 0 0 1-1 1A17 17 0 0 1 3 4a1 1 0 0 1 1-1h3.5a1 1 0 0 1 1 1c0 1.25.2 2.45.57 3.57a1 1 0 0 1-.25 1z"/></svg>000 000 0000</li>
        <li><svg viewBox="0 0 24 24"><path d="M7 1h10a2 2 0 0 1 2 2v18a2 2 0 0 1-2 2H7a2 2 0 0 1-2-2V3a2 2 0 0 1 2-2zm0 3v14h10V4z"/></svg>000 000 0000</li>
        <li><svg viewBox="0 0 24 24"><path d="M2 5h20v14H2zm2 2v.5l8 5 8-5V7z"/></svg>dhartley@meadowlark.com</li>
        <li><svg viewBox="0 0 24 24"><path d="M12 2a10 10 0 1 0 0 20 10 10 0 0 0 0-20zm6.9 9h-3a15 15 0 0 0-1.3-5.6A8 8 0 0 1 18.9 11zM12 4c.9 1.2 1.8 3.7 1.9 7h-3.8c.1-3.3 1-5.8 1.9-7zM9.4 5.4A15 15 0 0 0 8.1 11h-3a8 8 0 0 1 4.3-5.6zM5.1 13h3a15 15 0 0 0 1.3 5.6A8 8 0 0 1 5.1 13zM12 20c-.9-1.2-1.8-3.7-1.9-7h3.8c-.1 3.3-1 5.8-1.9 7zm2.6-1.4a15 15 0 0 0 1.3-5.6h3a8 8 0 0 1-4.3 5.6z"/></svg>www.meadowlark.com</li>
      </ul>
    </div>

    <div class="front__band"></div>
    <svg class="front__slash" viewBox="0 0 540 26" aria-hidden="true">
      <line x1="150" y1="26" x2="168" y2="0" stroke="#ffffff" stroke-width="3"/>
    </svg>
  </section>

  <section class="card card--back" aria-label="Appointment card">
    <div class="back__disc"></div>
    <p class="back__name"><span class="big">Meadowlark</span><span class="small">Aesthetics &amp; Wellness</span></p>
    <div class="appointment">
      <h2 class="appointment__title">Your Appointment</h2>
      <p class="appointment__note">Please give 24 hours notice if you need to reschedule.</p>
      <ul class="fields">
        <li>Name<span class="line"></span></li>
        <li>With<span class="line"></span></li>
        <li>Date<span class="line"></span></li>
        <li>Time<span class="line"></span></li>
      </ul>
    </div>
    <div class="back__band"></div>
  </section>
</main>
</body>
</html>
```